Dorsey K. Wendell Business Card

We need a business card for our company Dorsey K. Wendell Heating & Plumbing to be distributed to potential customers. It should follow the color scheme of our logo and have a modern upscale and masculine look.

The logo is attached and the info below should also be included:

5187 W. Cedar Brook Rd.
Manheim, PA 17545

Russell T. Wendell
(717) 592-0817
russelltwendell@fernmail.net
dorseykwendell.net
PA #093148

Industry/Entity Type

Business

Contact Information for Business Card

5187 W. Cedar Brook Rd.
Manheim, PA 17545

Russell T. Wendell
(717) 592-0817
russelltwendell@fernmail.net
dorseykwendell.net
PA #093148

Colors

Designer to choose colors to be used in the design.

Requirements
Must have
• Information above included

```html
<!DOCTYPE html>
<html lang="en">
<head>
<meta charset="utf-8">
<title>Dorsey K. Wendell Business Card</title>
<link rel="stylesheet" href="https://fonts.googleapis.com/css2?family=Nunito+Sans:wght@400;600;800&display=swap">
<style>
  :root {
    --brand-blue: #2a5a9b;
    --sky-blue: #8fd0f2;
    --lime: #9fcb3b;
    --paper: #ffffff;
    --ink: #2b2b2b;
    --backdrop: #e9e6e1;
  }
  * { box-sizing: border-box; margin: 0; padding: 0; }
  html, body { width: 1200px; height: 1200px; overflow: hidden; }
  body {
    background: var(--backdrop);
    font-family: "Nunito Sans", Arial, sans-serif;
    display: flex;
    flex-direction: column;
    align-items: center;
    justify-content: center;
    gap: 80px;
  }
  .card {
    position: relative;
    width: 840px;
    height: 480px;
    overflow: hidden;
  }
  .card--front {
    background: var(--brand-blue);
    display: flex;
    align-items: center;
    justify-content: center;
  }
  .brand {
    display: flex;
    align-items: center;
    gap: 18px;
  }
  .brand__mark {
    width: 64px;
    height: 64px;
    background: var(--lime);
    flex: none;
  }
  .brand__name {
    font-weight: 800;
    text-transform: uppercase;
    line-height: 1.05;
    letter-spacing: 0.02em;
  }
  .card--front .brand__name { color: var(--paper); font-size: 44px; }
  .card--back { background: var(--paper); }
  .card--back .brand {
    position: absolute;
    left: 44px;
    top: 44px;
  }
  .card--back .brand__mark { width: 52px; height: 52px; background: var(--brand-blue); }
  .card--back .brand__name { color: var(--brand-blue); font-size: 30px; }
  .wave {
    position: absolute;
    inset: 0;
    width: 100%;
    height: 100%;
  }
  .wave__stripe { fill: var(--sky-blue); }
  .wave__body { fill: var(--brand-blue); }
  .holder {
    position: absolute;
    left: 44px;
    top: 200px;
  }
  .holder__name {
    color: var(--brand-blue);
    font-weight: 600;
    font-size: 29px;
    letter-spacing: 0.01em;
  }
  .holder__phone {
    color: var(--ink);
    font-size: 23px;
    margin-top: 6px;
    letter-spacing: 0.03em;
  }
  .contact {
    position: absolute;
    right: 44px;
    top: 274px;
    text-align: right;
    color: var(--paper);
    font-size: 22px;
    line-height: 1.45;
    letter-spacing: 0.02em;
  }
  .contact__address { margin-bottom: 10px; }
</style>
</head>
<body>
  <section class="card card--front">
    <div class="brand">
      <span class="brand__mark"></span>
      <p class="brand__name">Dorsey K. Wendell<br>Heating &amp; Plumbing</p>
    </div>
  </section>

  <section class="card card--back">
    <svg class="wave" viewBox="0 0 840 480" preserveAspectRatio="none" aria-hidden="true">
      <path class="wave__stripe" d="M0,312 C180,356 330,300 470,238 C600,182 720,168 840,196 L840,226 C720,202 600,210 480,258 C330,318 180,378 0,336 Z"/>
      <path class="wave__body" d="M0,356 C200,400 340,330 490,262 C610,210 720,208 840,228 L840,480 L0,480 Z"/>
    </svg>

    <div class="brand">
      <span class="brand__mark"></span>
      <p class="brand__name">Dorsey K. Wendell<br>Heating &amp; Plumbing</p>
    </div>

    <div class="holder">
      <p class="holder__name">Russell T. Wendell</p>
      <p class="holder__phone">(717) 592-0817</p>
    </div>

    <div class="contact">
      <p class="contact__address">5187 W. Cedar Brook Rd.<br>Manheim, PA 17545</p>
      <p>russelltwendell@fernmail.net</p>
      <p>dorseykwendell.net</p>
      <p>PA #093148</p>
    </div>
  </section>
</body>
</html>
```